Ostrel Appraisals BV business cards (a financial services company)

I am looking for a business card design that stands out in the financial advisory field of business & intellectual property valuation. The business card design should be conservative, yet different. Address details have changed since the attached business card. New address is:

Molenvlietkade 27
4817 KT Leiden
The Netherlands

Telephone number remains the same.

```html
<!DOCTYPE html>
<html lang="en">
<head>
<meta charset="utf-8">
<title>Ostrel Appraisals BV – Business Cards</title>
<link href="https://fonts.googleapis.com/css2?family=Arimo:wght@400;700&display=swap" rel="stylesheet">
<style>
  :root {
    --backdrop: #1c1c1c;
    --card-dark: #3b3b3b;
    --card-darker: #2e2e2e;
    --card-light: #f7f7f7;
    --ink: #1a1a1a;
    --ink-soft: #444;
    --on-dark: #e6e6e6;
    --on-dark-soft: #c4c4c4;
  }
  * { box-sizing: border-box; margin: 0; padding: 0; }
  html, body { width: 1200px; height: 997px; overflow: hidden; }
  body {
    background: var(--backdrop);
    font-family: "Arimo", Arial, sans-serif;
    position: relative;
  }
  .card {
    position: absolute;
    width: 520px;
    height: 336px;
    border-radius: 3px;
    overflow: hidden;
    box-shadow: 0 14px 30px rgba(0,0,0,.55);
  }
  /* Back card */
  .card-back {
    left: 50px; top: 330px;
    background: var(--card-darker);
    display: flex; align-items: center; justify-content: center;
  }
  .wordmark {
    display: flex; align-items: center; gap: 12px;
    font-weight: 400; letter-spacing: 1px; text-transform: uppercase;
  }
  .wordmark .mark-square { width: 16px; height: 16px; background: currentColor; }
  .card-back .wordmark { color: #5c5c5c; font-size: 34px; }

  /* Front card */
  .card-front { left: 630px; top: 330px; background: var(--card-light); }
  .card-front .art { position: absolute; inset: 0; }
  .contact-block {
    position: absolute; right: 26px; top: 24px;
    text-align: right; color: var(--ink); font-size: 12.5px; line-height: 1.35;
  }
  .person-name { font-weight: 700; font-size: 15px; letter-spacing: .5px; }
  .person-role { color: var(--ink-soft); font-size: 11.5px; }
  .company-name { font-weight: 700; margin-top: 16px; }
  .address { color: var(--ink-soft); }
  .contact-lines { margin-top: 12px; }
  .contact-line { display: flex; justify-content: flex-end; align-items: center; gap: 7px; color: var(--ink-soft); }
  .contact-line.web { color: var(--ink); font-weight: 700; }
  .contact-line svg { width: 11px; height: 11px; fill: var(--ink); }
  .brand-block {
    position: absolute; left: 26px; bottom: 26px; color: var(--on-dark);
  }
  .card-front .wordmark { font-size: 26px; }
  .tagline { margin-top: 8px; font-size: 12.5px; color: var(--on-dark-soft); }
</style>
</head>
<body>
  <section class="card card-back" aria-label="Business card back">
    <div class="wordmark"><span class="mark-square"></span>Ostrel Appraisals</div>
  </section>

  <section class="card card-front" aria-label="Business card front">
    <svg class="art" viewBox="0 0 520 336" preserveAspectRatio="none" aria-hidden="true">
      <path d="M0,48 C150,140 330,235 520,246" fill="none" stroke="var(--card-dark)" stroke-width="11"/>
      <path d="M0,78 C140,165 320,255 520,262 L520,336 L0,336 Z" fill="var(--card-dark)"/>
    </svg>

    <div class="contact-block">
      <div class="person-name">MAARTEN VELDE</div>
      <div class="person-role">CFA, ASA, RV</div>
      <div class="person-role">Managing Director</div>
      <div class="company-name">Ostrel Appraisals</div>
      <div class="address">Molenvlietkade 27, 4817 KT Leiden</div>
      <div class="address">The Netherlands</div>
      <div class="contact-lines">
        <div class="contact-line">31 070 555 0184
          <svg viewBox="0 0 12 12"><path d="M1,3 C1,1 3,1 6,1 C9,1 11,1 11,3 L9,4 L8,3 L4,3 L3,4 Z M3,5 L9,5 L11,11 L1,11 Z"/></svg>
        </div>
        <div class="contact-line">mvelde@ostrelappraisals.com
          <svg viewBox="0 0 12 12"><path d="M0,2 H12 V10 H0 Z M1,3 L6,7 L11,3 Z" fill-rule="evenodd"/></svg>
        </div>
        <div class="contact-line web">www.ostrelappraisals.com
          <svg viewBox="0 0 12 12"><path d="M6,0 L12,6 H10 V12 H7 V8 H5 V12 H2 V6 H0 Z"/></svg>
        </div>
      </div>
    </div>

    <div class="brand-block">
      <div class="wordmark"><span class="mark-square"></span>Ostrel Appraisals</div>
      <div class="tagline">Business &amp; Intellectual Property Valuations</div>
    </div>
  </section>
</body>
</html>
```